Personal Injury Law Firm needs folder design

Need a folder design for our personal injury law firm, Horton & Quill, LLC. to give to all of our clients with their documents at the end of their case. I've attached our branding guide. We are branded as the 5 star law firm that fights for our clients like family. It should incorporate our colors or Green and White. We'd like to convey a message of moving on to the next chapter after finishing their case.

```html
<!DOCTYPE html>
<html lang="en">
<head>
<meta charset="utf-8">
<title>Horton &amp; Quill, LLC — Client Folder</title>
<link href="https://fonts.googleapis.com/css2?family=Cinzel:wght@600&family=Open+Sans:wght@400;600&family=Oswald:wght@500&family=Lato:wght@400;700&display=swap" rel="stylesheet">
<style>
  :root {
    --green: #18a87a;
    --white: #ffffff;
    --ink: #1f2a33;
    --text: #2b2b2b;
    --muted: #6b6b6b;
    --backdrop: #b7b6b7;
  }
  * { box-sizing: border-box; margin: 0; padding: 0; }
  html, body { width: 982px; height: 1200px; overflow: hidden; }
  body { background: var(--backdrop); position: relative; font-family: "Open Sans", sans-serif; }

  .spread {
    position: absolute; left: 61px; width: 860px;
    display: flex; box-shadow: 0 12px 30px rgba(0,0,0,.25);
  }
  .spread--outside { top: 40px; height: 520px; }
  .spread--inside { top: 620px; height: 540px; }

  .panel { position: relative; width: 430px; height: 100%; overflow: hidden; }
  .panel--back { background: var(--white); }
  .panel--front { background: var(--green); color: var(--white); }

  /* Back cover */
  .lockup { position: absolute; top: 150px; left: 40px; display: flex; align-items: center; gap: 12px; }
  .lockup__square { width: 64px; height: 56px; background: var(--green); flex: none; }
  .lockup__text { display: flex; flex-direction: column; gap: 4px; }
  .lockup__name {
    font-family: "Cinzel", serif; font-weight: 600; font-size: 24px; color: var(--green);
    border-bottom: 1.5px solid var(--ink); padding-bottom: 4px; white-space: nowrap;
  }
  .lockup__tagline { font-family: "Cinzel", serif; font-weight: 600; font-size: 9px; letter-spacing: 3px; color: var(--ink); text-align: center; }

  .contact { position: absolute; left: 0; right: 0; top: 330px; text-align: center; color: var(--text); font-size: 13px; line-height: 1.35; }
  .contact .icon { width: 12px; height: 12px; fill: var(--green); }
  .contact__icons { display: flex; justify-content: center; gap: 8px; margin: 14px 0 10px; }
  .contact__address { margin-top: 6px; }

  /* Front cover */
  .front__name {
    position: absolute; top: 130px; left: 0; right: 0; text-align: center;
    font-family: "Cinzel", serif; font-weight: 600; font-size: 44px; line-height: 1.1; color: var(--white);
  }
  .tagline {
    position: absolute; top: 320px; left: 0; right: 0; text-align: center;
    font-family: "Oswald", sans-serif; font-weight: 500; font-size: 30px;
    line-height: 1.3; letter-spacing: 3px; color: var(--ink);
  }

  /* Inside */
  .panel--inside-left { background: linear-gradient(90deg, #ffffff 0%, #e9e9e9 55%, #c9c9c9 100%); }
  .panel--inside-right { background: linear-gradient(90deg, #d4d4d4 0%, #f4f4f4 20%, #ffffff 100%); }
  .pocket { position: absolute; left: 0; bottom: 0; width: 430px; height: 190px; }

  .letter {
    position: absolute; top: 36px; left: 40px; width: 340px; height: 440px;
    background: var(--white); box-shadow: 2px 4px 10px rgba(0,0,0,.25);
    padding: 24px 22px; font-family: "Lato", sans-serif; color: var(--text); font-size: 7px; line-height: 1.35;
  }
  .letter__head { display: flex; justify-content: space-between; align-items: flex-start; }
  .letter__lockup { display: flex; align-items: center; gap: 6px; margin-top: 22px; }
  .letter__square { width: 28px; height: 24px; background: var(--green); }
  .letter__name { font-family: "Cinzel", serif; font-weight: 600; font-size: 11px; color: var(--green); border-bottom: 1px solid var(--ink); padding-bottom: 2px; }
  .letter__tagline { font-family: "Cinzel", serif; font-weight: 600; font-size: 4.5px; letter-spacing: 1.5px; color: var(--ink); text-align: center; margin-top: 2px; }
  .letter__contact { border-left: 1px solid var(--green); padding-left: 8px; font-size: 6px; color: var(--muted); }
  .letter__body { margin-top: 40px; }
  .letter__body p { margin-bottom: 8px; }
  .letter__salutation { font-weight: 700; font-size: 9px; }
</style>
</head>
<body>

<section class="spread spread--outside" aria-label="Folder outside">
  <div class="panel panel--back">
    <div class="lockup">
      <div class="lockup__square"></div>
      <div class="lockup__text">
        <span class="lockup__name">Horton &amp; Quill, LLC</span>
        <span class="lockup__tagline">ATTORNEYS AT LAW</span>
      </div>
    </div>

    <div class="contact">
      <svg class="icon" viewBox="0 0 24 24" aria-hidden="true"><path d="M12 2a7 7 0 0 0-7 7c0 5 7 13 7 13s7-8 7-13a7 7 0 0 0-7-7zm0 9.5A2.5 2.5 0 1 1 12 6.5a2.5 2.5 0 0 1 0 5z"/></svg>
      <p class="contact__address">418 Harborline Avenue<br>Bayview, FL 34012</p>
      <div class="contact__icons" aria-hidden="true">
        <svg class="icon" viewBox="0 0 24 24"><path d="M6.6 10.8a15 15 0 0 0 6.6 6.6l2.2-2.2a1 1 0 0 1 1-.25 11.4 11.4 0 0 0 3.6.57 1 1 0 0 1 1 1V20a1 1 0 0 1-1 1A17 17 0 0 1 3 4a1 1 0 0 1 1-1h3.5a1 1 0 0 1 1 1c0 1.25.2 2.45.57 3.57a1 1 0 0 1-.25 1z"/></svg>
        <svg class="icon" viewBox="0 0 24 24"><path d="M3 5h18v14H3zm2 2v.5l7 4.5 7-4.5V7z"/></svg>
        <svg class="icon" viewBox="0 0 24 24"><g fill="none" stroke="var(--green)" stroke-width="2"><circle cx="12" cy="12" r="9"/><ellipse cx="12" cy="12" rx="4" ry="9"/><path d="M3 12h18"/></g></svg>
      </div>
      <p>(555) 014-2290<br>mara@hortonquill.com<br>www.hortonquill.com</p>
    </div>
  </div>

  <div class="panel panel--front">
    <h1 class="front__name">Horton<br>&amp; Quill</h1>
    <p class="tagline">YOUR NEXT CHAPTER<br>STARTS HERE</p>
  </div>
</section>

<section class="spread spread--inside" aria-label="Folder inside">
  <div class="panel panel--inside-left">
    <svg class="pocket" viewBox="0 0 430 190" aria-hidden="true">
      <path d="M0 70 L340 10 Q360 6 370 20 L430 130 L430 190 L0 190 Z" fill="var(--green)"/>
    </svg>
  </div>

  <div class="panel panel--inside-right">
    <article class="letter">
      <div class="letter__head">
        <div class="letter__lockup">
          <div class="letter__square"></div>
          <div>
            <div class="letter__name">Horton &amp; Quill, LLC</div>
            <div class="letter__tagline">ATTORNEYS AT LAW</div>
          </div>
        </div>
        <div class="letter__contact">
          Your address, City<br>State, Zip 1234<br>123 456 789<br>info@yourgmail.com<br>www.yourwebsite.com
        </div>
      </div>
      <div class="letter__body">
        <p>January-03-2020</p>
        <p>Mr. John Doe<br>President</p>
        <p>Link Corporation<br>123 Street Name, Suite# 10<br>City, State, 120023</p>
        <p class="letter__salutation">Dear Mr. John</p>
        <p>Lorem ipsum dolor sit amet, consectetur adipiscing elit, sed do eiusmod tempor incididunt ut labore et dolore magna aliqua. Ut enim ad minim veniam, quis nostrud exercitation ullamco laboris nisi ut aliquip ex ea commodo consequat.</p>
        <p>Lorem ipsum dolor sit amet, consectetur adipiscing elit, sed do eiusmod tempor incididunt ut labore et dolore magna aliqua. Duis aute irure dolor in reprehenderit in voluptate velit esse cillum dolore eu fugiat nulla pariatur.</p>
        <p>Excepteur sint occaecat cupidatat non proident, sunt in culpa qui officia deserunt mollit anim id est laborum.</p>
      </div>
    </article>
    <svg class="pocket" viewBox="0 0 430 190" aria-hidden="true">
      <path d="M20 60 Q24 40 45 38 L430 0 L430 190 L0 190 Z" fill="var(--green)"/>
    </svg>
  </div>
</section>

</body>
</html>
```